Christmas Party Poster

I am promoting a Christmas Party for teenagers age 13-17 years old. The event is the first of its kind in our area, Weston Super Mare. The ticket price is to include food, soft drink's, music, entertainment.

There is nothing else of its kind in the the area or surrounding towns so a one of a kind event and new to the town. I would like the poster to be as simple and less busy as possible while still clearly showing the key information, anything that can be added it to show its a Christmas party for teenagers would be great. Also this is aimed at 13-17 year old's so as current and modern a design as possible.
Updates

A big thank you for the designs so far, As this is my first project I'm just getting the hang of what to ask for. I have slightly updated the brief and I now realize less is more, so long as the poster has the key elements of event name, date, time's, location, price and age range. The rest I should have been more flexible on. Thank you for your patience.

Target Market(s)

My Target Market are teenagers specifically 13-17 year olds

Industry/Entity Type

Town

Requirements
Must have
• The Title 'Frostgleam' The venue is 'The Amber Pavilion h-b-t', Phone Number '01852 630284' Date '19th December'. Times '19.00 - 23.00'. Strictly u18 or age 13-17 years. Ticket price of £20. Friendspace 'frost gleam hbt' limited 4 tickets per person
Nice to have
• Christmas Party, Photo of your night out. Food and drink included
Should not have
• no worded reference to Santa, snowmen, reindeer, disco, try to keep out as not to offend cool teenagers.

```html
<!DOCTYPE html>
<html lang="en">
<head>
<meta charset="utf-8">
<title>Frostgleam – Christmas Party Poster</title>
<link rel="stylesheet" href="https://fonts.googleapis.com/css2?family=Anton&family=Arimo:wght@700&family=Roboto+Condensed:ital,wght@0,700;1,700&display=swap">
<style>
  :root {
    --night-deep: #060f22;
    --night-mid: #14315c;
    --night-glow: #3a6eaa;
    --neon-green: #2ee84a;
    --band-green: #3bf060;
    --ink-white: #ffffff;
    --chrome-light: #f4f8ff;
    --chrome-mid: #9fb4d4;
    --chrome-dark: #4d6790;
    --mark-blue: #4f7fc0;
  }
  * { margin: 0; padding: 0; box-sizing: border-box; }
  html, body {
    width: 848px; height: 1200px; overflow: hidden;
    background: var(--night-deep);
  }
  .poster {
    position: relative; width: 848px; height: 1200px; overflow: hidden;
    font-family: "Arimo", Arial, sans-serif;
    font-weight: 700;
    color: var(--ink-white);
  }
  .starfield {
    position: absolute; inset: 0;
    background:
      radial-gradient(circle at 50% 24%, rgba(200,225,255,.6) 0, rgba(90,140,210,.28) 10%, transparent 30%),
      radial-gradient(ellipse at 30% 72%, rgba(70,120,190,.45) 0, transparent 45%),
      radial-gradient(ellipse at 80% 55%, rgba(60,110,180,.35) 0, transparent 40%),
      linear-gradient(180deg, var(--night-deep) 0%, var(--night-mid) 35%, #1b3d6e 60%, var(--night-deep) 100%);
  }
  .band { position: absolute; inset: 0; }
  .venue {
    position: absolute; top: 36px; left: 0; width: 100%;
    text-align: center;
    font-variant: small-caps;
    color: var(--neon-green);
    font-size: 27px; line-height: 30px; letter-spacing: 2px;
    text-shadow: 1px 1px 0 #000, 0 0 3px #000;
  }
  .title {
    position: absolute; left: 430px; top: 330px;
    transform: translate(-50%, -50%) rotate(-19deg) skewX(-10deg);
    font-family: "Anton", Impact, sans-serif;
    font-weight: 400;
    font-size: 166px; line-height: 1; letter-spacing: 1px;
    text-transform: uppercase; white-space: nowrap;
    background: linear-gradient(180deg, var(--chrome-light) 0%, var(--chrome-mid) 45%, var(--chrome-dark) 52%, var(--chrome-light) 100%);
    -webkit-background-clip: text; background-clip: text;
    color: transparent;
    -webkit-text-stroke: 3px #e8eef8;
    filter: drop-shadow(4px 6px 4px rgba(0,0,0,.6));
  }
  .ticket-limit {
    position: absolute; left: 560px; top: 494px; width: 240px;
    text-align: center; font-size: 20px; line-height: 25px;
    transform: rotate(-5deg);
  }
  .age-block {
    position: absolute; left: 210px; top: 620px; width: 438px; height: 88px;
    border-top: 2px solid var(--ink-white); border-bottom: 2px solid var(--ink-white);
    display: flex; align-items: center; justify-content: center;
  }
  .age-range { color: var(--neon-green); font-size: 38px; }
  .features {
    position: absolute; left: 62px; top: 740px; width: 820px;
    font-family: "Roboto Condensed", "Arial Narrow", sans-serif;
    font-weight: 700;
    transform: rotate(6deg); transform-origin: left top;
    line-height: 1;
  }
  .features .lead { font-size: 42px; white-space: nowrap; letter-spacing: -.5px; }
  .features .lead small { font-size: 29px; }
  .features .extra {
    font-size: 40px; color: var(--neon-green); margin-top: 2px; margin-left: -12px;
    font-style: italic; white-space: nowrap;
  }
  .social {
    position: absolute; left: 66px; top: 930px;
    display: flex; align-items: center; gap: 14px;
  }
  .social-mark {
    width: 56px; height: 56px; border-radius: 8px;
    background: var(--mark-blue); border: 2px solid #cfd8e6;
  }
  .social-text { font-size: 14px; line-height: 18px; }
  .event-details {
    position: absolute; right: 48px; top: 930px;
    text-align: right;
  }
  .event-date { font-size: 24px; line-height: 30px; color: var(--neon-green); }
  .event-phone { font-size: 18px; line-height: 26px; }
  .pricing {
    position: absolute; left: 0; top: 1034px; width: 100%;
    text-align: center; font-size: 31px; line-height: 42px;
  }
</style>
</head>
<body>
<main class="poster">
  <div class="starfield" role="img" aria-label="Deep blue starry night sky with soft swirling light"></div>

  <svg class="band" width="848" height="1200" viewBox="0 0 848 1200" aria-hidden="true">
    <polygon points="0,640 848,36 848,70 0,676" fill="var(--band-green)"/>
  </svg>

  <p class="venue">Venue:<br>The Amber Pavilion h-b-t</p>

  <h1 class="title">Frostgleam</h1>

  <p class="ticket-limit">Limited 4 Tickets<br>Per Person</p>

  <div class="age-block"><p class="age-range">Ages 13-17 years</p></div>

  <div class="features">
    <p class="lead"><small>The </small>Best Music, Top Tunes... Entertainment,</p>
    <p class="extra">Photo Of Your Night Out</p>
  </div>

  <div class="social">
    <span class="social-mark"></span>
    <p class="social-text">Find Us On<br>Friendspace 'frost gleam hbt'</p>
  </div>

  <div class="event-details">
    <p class="event-date">19th December · 19.00 - 23.00</p>
    <p class="event-phone">Tickets: 01852 630284</p>
  </div>

  <p class="pricing">All Food And Drink Included<br>In Ticket Price Of £20</p>
</main>
</body>
</html>
```